Business Cards

Business cards (double-sided) to be handed out to clients and potential clients, with contact details, logo .

Target Market(s)

Small to medium size businesses

Industry/Entity Type

Accountants

Contact Information for Business Card

Brightwater Ledger & Counsel Ltd

Colors

Designer to choose only greyscale colors for use in the design.

Requirements
Must have
• Name, Title, Address, Phone number, Email, Website
Nice to have
• Modern, clean lines, classy
Should not have
• Business cards to be double-sided. Form keeps reverting to single-sided.

```html
<!DOCTYPE html>
<html lang="en">
<head>
<meta charset="utf-8">
<title>Brightwater Ledger &amp; Counsel – Business Cards</title>
<link href="https://fonts.googleapis.com/css2?family=Arimo:wght@400;700&family=Jost:wght@400&display=swap" rel="stylesheet">
<style>
  :root {
    --backdrop: #dadada;
    --card-top: #ffffff;
    --card-bottom: #e3e3e3;
    --charcoal: #4a4a4a;
    --rule-grey: #6b6b6b;
    --ink: #111111;
    --paper: #ffffff;
  }
  * { margin: 0; padding: 0; box-sizing: border-box; }
  html, body { width: 1200px; height: 1200px; overflow: hidden; background: var(--backdrop); }
  .canvas { position: relative; width: 1200px; height: 1200px; }
  .card {
    position: absolute; left: 275px; width: 595px; height: 340px;
    background: linear-gradient(to bottom, var(--card-top), var(--card-bottom));
    overflow: hidden;
  }
  .card--front { top: 177px; }
  .card--back { top: 627px; }

  .side-band { position: absolute; left: 0; top: 0; width: 51px; height: 100%; background: var(--charcoal); }
  .wordmark {
    position: absolute; left: 51px; right: 0; top: 0; bottom: 0;
    display: flex; flex-direction: column; align-items: center; justify-content: center;
    font-family: "Jost", sans-serif; font-weight: 400; color: var(--ink);
    text-transform: uppercase; text-align: center;
  }
  .wordmark__name { font-size: 38px; letter-spacing: 4px; line-height: 1.1; }
  .wordmark__tag { font-size: 11px; letter-spacing: 3px; margin-top: 6px; }

  .company-block {
    position: absolute; left: 40px; top: 34px; width: 140px;
    text-align: right; font-family: "Arimo", sans-serif; color: var(--ink);
  }
  .company-block__name { font-size: 20px; font-weight: 700; line-height: 25px; }
  .company-block__rule { height: 7px; background: var(--rule-grey); margin: 14px 0 12px; }
  .company-block__title { font-size: 18px; font-weight: 400; }
  .avatar { position: absolute; left: 193px; top: 35px; width: 37px; height: 37px; }

  .contact-panel {
    position: absolute; left: 267px; top: 160px; right: 0; bottom: 0;
    background: var(--charcoal); padding: 24px 0 0 18px;
    font-family: "Arimo", sans-serif; color: var(--paper); list-style: none;
  }
  .contact-panel li { display: flex; align-items: center; height: 31px; font-size: 18px; }
  .contact-panel svg { width: 21px; height: 21px; margin-right: 11px; flex: none; }
</style>
</head>
<body>
<main class="canvas">
  <section class="card card--front" aria-label="Card front">
    <div class="side-band"></div>
    <div class="wordmark">
      <span class="wordmark__name">Brightwater</span>
      <span class="wordmark__tag">Ledger &amp; Counsel</span>
    </div>
  </section>

  <section class="card card--back" aria-label="Card back">
    <div class="company-block">
      <p class="company-block__name">Brightwater Ledger &amp; Counsel Ltd</p>
      <div class="company-block__rule"></div>
      <p class="company-block__title">Accountants</p>
    </div>
    <svg class="avatar" viewBox="0 0 40 40" aria-hidden="true">
      <circle cx="20" cy="20" r="19" fill="#666" stroke="#fff" stroke-width="2"/>
      <circle cx="20" cy="15" r="6" fill="#fff"/>
      <path d="M9 30 Q9 22 20 22 Q31 22 31 30 Z" fill="#fff"/>
    </svg>

    <ul class="contact-panel">
      <li>
        <svg viewBox="0 0 20 20" aria-hidden="true"><circle cx="10" cy="10" r="10" fill="#fff"/><path d="M10 4.5a3.5 3.5 0 0 0-3.5 3.5c0 2.6 3.5 6.5 3.5 6.5s3.5-3.9 3.5-6.5A3.5 3.5 0 0 0 10 4.5z" fill="#4a4a4a"/><circle cx="10" cy="8" r="1.3" fill="#fff"/></svg>
        2740 Alder Crescent
      </li>
      <li>
        <svg viewBox="0 0 20 20" aria-hidden="true"><circle cx="10" cy="10" r="10" fill="#fff"/><path d="M7 5l2 2.5-1.2 1.3c.6 1.4 1.6 2.5 3 3.2L12 10.8l2.4 2-1 1.7c-3.7-.3-7.3-4.3-7.5-8.2z" fill="#4a4a4a"/></svg>
        +43-0612 4470285
      </li>
      <li>
        <svg viewBox="0 0 20 20" aria-hidden="true"><circle cx="10" cy="10" r="10" fill="#fff"/><rect x="5" y="6.5" width="10" height="7" rx="1" fill="#4a4a4a"/><path d="M5.5 7l4.5 3.5L14.5 7" fill="none" stroke="#fff" stroke-width="1"/></svg>
        hello@brightwaterledger.net
      </li>
      <li>
        <svg viewBox="0 0 20 20" aria-hidden="true"><circle cx="10" cy="10" r="10" fill="#fff"/><circle cx="10" cy="10" r="5" fill="none" stroke="#4a4a4a" stroke-width="1.4"/><path d="M5 10h10M10 5c-2 2.5-2 7.5 0 10M10 5c2 2.5 2 7.5 0 10" fill="none" stroke="#4a4a4a" stroke-width="1"/></svg>
        www.brightwaterledger.com
      </li>
    </ul>
  </section>
</main>
</body>
</html>
```